Graph Template Design

We are looking for a modern and flat theme of the attached image/graph/flowchart. It does not have to be in the same format or layout but needs to show the same flows.

We are a small digital agency based in Malta (Tarvo Link). We service clients with online media and marketing strategies and the basis of this project is to use the design for a client proposal document which is being reworked.

Design Specifics: I have submitted my design and the specs inside the proposal. We are looking for a designer to redesign the attached image in our proposal set
up with you yesterday. I have submitted an existing design and also submitted my preferred colors etc. Please see the submission we made.

Target Market(s)

We are looking for designs to compliment oir business proposal for our new and existing clients.

Industry/Entity Type

Media

Font styles to use
Sans Serif

Colors
0555a3
3276b5
33a6d7
9bcb3b
85cae6
abd036

Requirements
Must have
• we need to keep the flow of the graph the same but it can be redesigned to make it look more modern etc
Nice to have
• flat design

```html
<!DOCTYPE html>
<html lang="en">
<head>
<meta charset="utf-8">
<title>Tarvo Link – Content Distribution Flow</title>
<link href="https://fonts.googleapis.com/css2?family=Open+Sans:wght@400;600;700&display=swap" rel="stylesheet">
<style>
  :root{
    --navy:#0555a3;
    --blue:#3276b5;
    --sky:#33a6d7;
    --sky-soft:#85cae6;
    --green:#9bcb3b;
    --lime:#abd036;
    --ring:#dbeef7;
    --hub-ring:#cfe6f1;
    --line:#9fc3d6;
    --ink:#2f3a45;
    --white:#ffffff;
  }
  html,body{margin:0;padding:0;overflow:hidden;background:var(--white);}
  .canvas{width:1200px;height:813px;position:relative;overflow:hidden;font-family:"Open Sans",Arial,sans-serif;}
  .flow{display:block;width:1200px;height:813px;}
  .flow text{font-family:"Open Sans",Arial,sans-serif;}
  .link{fill:none;stroke:var(--line);stroke-width:2;stroke-dasharray:5 4;}
  .chain{fill:none;stroke:var(--ring);stroke-width:14;stroke-linejoin:round;}
  .node-ring{fill:var(--ring);}
  .node-core{fill:var(--sky);}
  .node-label{font-size:11px;fill:var(--ink);}
  .glyph{fill:none;stroke:var(--white);stroke-width:2.6;stroke-linecap:round;stroke-linejoin:round;}
  .glyph-fill{fill:var(--white);}
  .hub-ring{fill:var(--white);stroke:var(--hub-ring);stroke-width:3;}
  .hub-social{fill:var(--green);}
  .hub-news{fill:var(--blue);}
  .hub-mark{fill:var(--lime);}
  .hub-label{font-size:17px;font-weight:600;fill:var(--white);text-anchor:middle;}
  .brand-ring{fill:none;stroke:var(--navy);stroke-width:2;}
  .brand-name{font-size:33px;font-weight:700;fill:var(--navy);text-anchor:middle;}
  .dot{stroke:var(--ring);stroke-width:3;}
  .dot-navy{fill:var(--navy);}
  .dot-green{fill:var(--green);}
  .dot-blue{fill:var(--blue);}
  .dot-lime{fill:var(--lime);}
  .dot-sky{fill:var(--sky);}
</style>
</head>
<body>
<div class="canvas">
<svg class="flow" viewBox="0 0 1500 1013" xmlns="http://www.w3.org/2000/svg" aria-label="Tarvo Link content distribution flow">
  <defs>
    <marker id="arrow" viewBox="0 0 10 10" refX="8" refY="5" markerWidth="7" markerHeight="7" orient="auto">
      <path d="M1 1 L8 5 L1 9" fill="none" stroke="#9fc3d6" stroke-width="1.8"/>
    </marker>
    <g id="node"><circle class="node-ring" r="44"/><circle class="node-core" r="36"/></g>
    <g id="i-screen"><rect class="glyph" x="-17" y="-13" width="34" height="22" rx="2"/><path class="glyph" d="M-7 15h14M0 9v6"/></g>
    <g id="i-play"><rect class="glyph" x="-17" y="-13" width="34" height="24" rx="2"/><path class="glyph-fill" d="M-5 -7 L7 -1 L-5 5z"/></g>
    <g id="i-mail"><rect class="glyph" x="-16" y="-10" width="32" height="22" rx="2"/><path class="glyph" d="M-16 -10 L0 3 L16 -10"/></g>
    <g id="i-gear"><circle class="glyph" r="9"/><circle class="glyph-fill" r="3"/><path class="glyph" d="M0 -15v4M0 11v4M-15 0h4M11 0h4"/></g>
    <g id="i-search"><circle class="glyph" cx="-3" cy="-3" r="10"/><path class="glyph" d="M5 5 L14 14"/></g>
    <g id="i-user"><circle class="glyph" cy="-7" r="6"/><path class="glyph" d="M-12 14c0-9 5-13 12-13s12 4 12 13z"/></g>
    <g id="i-pic"><rect class="glyph" x="-16" y="-12" width="32" height="24" rx="2"/><path class="glyph" d="M-12 8 L-3 -1 L4 6 L8 2 L13 8"/></g>
    <g id="i-code"><rect class="glyph" x="-17" y="-12" width="34" height="22" rx="2"/><path class="glyph" d="M-5 -5 L-10 -1 L-5 3M5 -5 L10 -1 L5 3"/></g>
    <g id="i-target"><circle class="glyph" r="13"/><circle class="glyph" r="6"/><circle class="glyph-fill" r="2"/></g>
    <g id="i-nodes"><circle class="glyph-fill" r="5"/><path class="glyph" d="M0 0 L-12 -10M0 0 L12 -9M0 0 L-11 11M0 0 L13 10"/><circle class="glyph-fill" cx="-12" cy="-10" r="3"/><circle class="glyph-fill" cx="12" cy="-9" r="3"/><circle class="glyph-fill" cx="-11" cy="11" r="3"/><circle class="glyph-fill" cx="13" cy="10" r="3"/></g>
    <g id="i-chat"><path class="glyph" d="M-15 -11h20v14h-12l-6 5v-5h-2z"/><path class="glyph" d="M9 -3h6v13h-2v4l-5-4h-9v-5"/></g>
    <g id="i-check"><path class="glyph" d="M0 -15 L13 -10 V2 C13 9 6 14 0 16 C-6 14 -13 9 -13 2 V-10z"/><path class="glyph" d="M-6 0 L-1 5 L8 -5"/></g>
    <g id="i-globe"><circle class="glyph" r="13"/><path class="glyph" d="M-13 0h26M0 -13c-6 7-6 19 0 26M0 -13c6 7 6 19 0 26"/></g>
    <g id="i-page"><rect class="glyph" x="-17" y="-13" width="34" height="26" rx="2"/><path class="glyph" d="M-17 -6h34M-12 0h10v7h-10zM3 1h9M3 6h9"/></g>
    <g id="i-pie"><circle class="glyph" r="14"/><path class="glyph" d="M0 0 V-14M0 0 L12 7"/></g>
    <g id="i-bars"><path class="glyph" d="M-14 14h28M-10 12v-10M-3 12v-16M4 12v-7M11 12v-13"/></g>
    <g id="i-link"><rect class="glyph" x="-14" y="-5" width="16" height="10" rx="5" transform="rotate(-45)"/><rect class="glyph" x="-2" y="-5" width="16" height="10" rx="5" transform="rotate(-45)"/></g>
    <g id="i-box"><path class="glyph" d="M-14 -8 L0 -15 L14 -8 V9 L0 16 L-14 9z M-14 -8 L0 -1 L14 -8 M0 -1 V16"/></g>
    <g id="i-board"><rect class="glyph" x="-11" y="-13" width="22" height="28" rx="2"/><path class="glyph" d="M-5 -16h10v5h-10z"/></g>
    <g id="i-book"><rect class="glyph" x="-13" y="-14" width="24" height="28" rx="2"/><path class="glyph" d="M-6 6 L8 -10"/></g>
  </defs>

  <g class="links">
    <path class="link" d="M199 376 C260 190 470 118 708 117" marker-end="url(#arrow)"/>
    <path class="link" d="M708 145 C480 150 290 250 232 398" marker-end="url(#arrow)"/>
    <path class="link" d="M199 631 C260 818 470 890 708 890" marker-end="url(#arrow)"/>
    <path class="link" d="M708 862 C480 858 290 760 232 610" marker-end="url(#arrow)"/>
    <path class="link" d="M527 296 L272 434" marker-end="url(#arrow)"/>
    <path class="link" d="M527 714 L272 577" marker-end="url(#arrow)"/>
    <path class="link" d="M290 489 L383 489" marker-end="url(#arrow)"/>
    <path class="link" d="M380 521 L287 521" marker-end="url(#arrow)"/>
    <path class="link" d="M695 232 L743 177" marker-end="url(#arrow)"/>
    <path class="link" d="M540 418 L564 389" marker-end="url(#arrow)"/>
    <path class="link" d="M540 590 L566 622" marker-end="url(#arrow)"/>
    <path class="link" d="M695 776 L743 831" marker-end="url(#arrow)"/>
    <path class="link" d="M1044 503 L586 503" marker-end="url(#arrow)"/>
    <path class="link" d="M1045 497 L725 326" marker-end="url(#arrow)"/>
    <path class="link" d="M1045 509 L725 680" marker-end="url(#arrow)"/>
  </g>

  <g class="brand">
    <circle class="brand-ring" cx="153" cy="503" r="123"/>
    <circle class="brand-ring" cx="153" cy="503" r="108"/>
    <text class="brand-name" x="153" y="515">Tarvo Link</text>
  </g>

  <g class="hub">
    <circle class="hub-ring" cx="624" cy="309" r="85"/>
    <circle class="hub-social" cx="624" cy="309" r="72"/>
    <rect class="glyph-fill" x="598" y="259" width="12" height="12" rx="2"/>
    <rect class="glyph-fill" x="619" y="253" width="12" height="12" rx="2"/>
    <rect class="glyph-fill" x="594" y="280" width="12" height="12" rx="2"/>
    <rect class="glyph-fill" x="598" y="301" width="12" height="12" rx="2"/>
    <path class="glyph" d="M617 282 L640 272 V300 L617 290z M640 278 h6 M646 286 h-6"/>
    <text class="hub-label" x="624" y="346">Social Media</text>
  </g>
  <g class="hub">
    <circle class="hub-ring" cx="481" cy="503" r="90"/>
    <circle class="hub-news" cx="481" cy="503" r="72"/>
    <rect class="glyph" x="455" y="462" width="52" height="38" rx="3"/>
    <path class="glyph" d="M455 472h52"/>
    <circle class="glyph" cx="481" cy="492" r="7"/>
    <text class="hub-label" x="481" y="542">News Portal</text>
  </g>
  <g class="hub">
    <circle class="hub-ring" cx="624" cy="697" r="85"/>
    <circle class="hub-social" cx="624" cy="697" r="72"/>
    <circle class="glyph" cx="624" cy="672" r="17"/>
    <path class="glyph-fill" d="M624 662 L627 669 L634 669 L628 674 L630 681 L624 677 L618 681 L620 674 L614 669 L621 669z"/>
    <path class="glyph" d="M615 688 L611 706 L617 702 L620 708 L622 690M633 688 L637 706 L631 702 L628 708 L626 690"/>
    <text class="hub-label" x="624" y="737">Bookmarking</text>
  </g>

  <g class="dots">
    <circle class="dot dot-navy" cx="199" cy="386" r="9"/>
    <circle class="dot dot-navy" cx="278" cy="489" r="9"/>
    <circle class="dot dot-navy" cx="199" cy="621" r="9"/>
    <circle class="dot dot-green" cx="685" cy="243" r="9"/>
    <circle class="dot dot-green" cx="537" cy="292" r="9"/>
    <circle class="dot dot-blue" cx="531" cy="428" r="9"/>
    <circle class="dot dot-blue" cx="391" cy="521" r="9"/>
    <circle class="dot dot-blue" cx="531" cy="579" r="9"/>
    <circle class="dot dot-green" cx="537" cy="718" r="9"/>
    <circle class="dot dot-green" cx="685" cy="765" r="9"/>
    <circle class="dot dot-sky" cx="718" cy="145" r="9"/>
    <circle class="dot dot-sky" cx="1055" cy="503" r="9"/>
    <circle class="dot dot-sky" cx="718" cy="862" r="9"/>
  </g>

  <path class="chain" d="M782 130 L1155 503 L782 871"/>
  <path class="chain" d="M976 80 L1348 445 L1400 505 L1348 560 L976 925"/>

  <g class="outlets">
    <use href="#node" x="782" y="130"/><use href="#i-box" x="782" y="130"/>
    <text class="node-label" x="834" y="126">Products/Services<tspan x="834" dy="14">Websites &amp; Pages</tspan></text>
    <use href="#node" x="857" y="203"/><use href="#i-user" x="857" y="203"/>
    <text class="node-label" x="908" y="198">Staff/Key<tspan x="908" dy="14">Personnel Profiling</tspan></text>
    <use href="#node" x="931" y="278"/><use href="#i-code" x="931" y="278"/>
    <text class="node-label" x="981" y="274">Directories/Webmaster<tspan x="981" dy="14">Listings &amp; Profiles</tspan></text>
    <use href="#node" x="1006" y="352"/><use href="#i-target" x="1006" y="352"/>
    <text class="node-label" x="1056" y="347">Authority<tspan x="1056" dy="14">Domains</tspan></text>
    <use href="#node" x="1080" y="428"/><use href="#i-gear" x="1080" y="428"/>
    <text class="node-label" x="1130" y="422">Industry Related<tspan x="1130" dy="14">Content</tspan></text>
    <use href="#node" x="1155" y="503"/><use href="#i-user" x="1155" y="503"/>
    <text class="node-label" x="1204" y="502">Employment<tspan x="1204" dy="14">Profiles/Listings</tspan></text>
    <use href="#node" x="1080" y="578"/><use href="#i-pic" x="1080" y="578"/>
    <text class="node-label" x="1129" y="585">Photo Sharing<tspan x="1129" dy="14">Profiles</tspan></text>
    <use href="#node" x="1006" y="650"/><use href="#i-board" x="1006" y="650"/>
    <text class="node-label" x="1055" y="652">White<tspan x="1055" dy="14">Papers</tspan></text>
    <use href="#node" x="931" y="724"/><use href="#i-book" x="931" y="724"/>
    <text class="node-label" x="981" y="724">Case<tspan x="981" dy="14">Studies</tspan></text>
    <use href="#node" x="857" y="797"/><use href="#i-link" x="857" y="797"/>
    <text class="node-label" x="906" y="799">RSS<tspan x="906" dy="14">Syndication</tspan></text>
    <use href="#node" x="782" y="871"/><use href="#i-screen" x="782" y="871"/>
    <text class="node-label" x="833" y="879">Static<tspan x="833" dy="14">Websites</tspan></text>

    <use href="#node" x="976" y="80"/><use href="#i-page" x="976" y="80"/>
    <text class="node-label" x="1027" y="73">Onsite News<tspan x="1027" dy="14">Pages</tspan></text>
    <use href="#node" x="1050" y="155"/><use href="#i-play" x="1050" y="155"/>
    <text class="node-label" x="1102" y="153">Video/Movie<tspan x="1102" dy="14">Profiles</tspan></text>
    <use href="#node" x="1125" y="228"/><use href="#i-mail" x="1125" y="228"/>
    <text class="node-label" x="1176" y="223">Newsletter/Email<tspan x="1176" dy="14">Campaigns</tspan></text>
    <use href="#node" x="1199" y="300"/><use href="#i-nodes" x="1199" y="300"/>
    <text class="node-label" x="1250" y="297">High Value Industry<tspan x="1250" dy="14">Related Backlinks</tspan></text>
    <use href="#node" x="1273" y="377"/><use href="#i-search" x="1273" y="377"/>
    <text class="node-label" x="1325" y="372">Competitor<tspan x="1325" dy="14">Content</tspan></text>
    <use href="#node" x="1348" y="445"/><use href="#i-chat" x="1348" y="445"/>
    <text class="node-label" x="1392" y="440">Ratings/Reviews<tspan x="1392" dy="14">Profiles</tspan></text>
    <use href="#node" x="1348" y="560"/><use href="#i-check" x="1348" y="560"/>
    <text class="node-label" x="1392" y="561">Classified/Open<tspan x="1392" dy="14">Site Listings</tspan></text>
    <use href="#node" x="1273" y="630"/><use href="#i-globe" x="1273" y="630"/>
    <text class="node-label" x="1324" y="630">Search Engine<tspan x="1324" dy="14">Profiles</tspan></text>
    <use href="#node" x="1199" y="702"/><use href="#i-page" x="1199" y="702"/>
    <text class="node-label" x="1249" y="705">Wiki<tspan x="1249" dy="14">Pages</tspan></text>
    <use href="#node" x="1125" y="777"/><use href="#i-pie" x="1125" y="777"/>
    <text class="node-label" x="1175" y="780">Info<tspan x="1175" dy="14">Graphics</tspan></text>
    <use href="#node" x="1050" y="852"/><use href="#i-bars" x="1050" y="852"/>
    <text class="node-label" x="1100" y="855">Data/Analytics<tspan x="1100" dy="14">Sharing</tspan></text>
    <use href="#node" x="976" y="925"/><use href="#i-page" x="976" y="925"/>
    <text class="node-label" x="1025" y="927">Web 2.0<tspan x="1025" dy="14">Pages</tspan></text>
  </g>
</svg>
</div>
</body>
</html>
```